Packaging label for spirit line

We currently have a various line of spirits and are looking to rebrand the label. The bottle would stay the same since there is a lot of stock. An example of the current situation has been attached. The entire collection is to be found on our website: www.velvetparlor.quinmark.be/spirits

These spirits are a product created by our cocktail bar "Velvet Parlor". The name however, would likely change to "Tipplefox" or plural "Tipplefoxes" since we'd like to split those 2 businesses. The series "shaker lineup" would remain the same as it is a complete series mainly invented for mixology.

The current label is fine, but needs that extra spark that makes it stand out on a shelve compared to other spirit bottles. We envision a more funky yet sophisticated branding with perhaps goldtrims for that "exclusive, luxurious" feel and very much like a vintage animal humification vibe (for example: the marigold or fennick's). Preferably a french bulldog as this has been our mascotte since the very beginning of starting this business.

Last but not least, the measurements: max. 90 mm height and max. 260 mm length. The current label is 90x180mm. 260mm means the label goes fully around the bottle.

Industry/Entity Type

Alcoholic Beverages

Font styles to use
Serif
Sans Serif

Requirements
Must have
• The label must have the standard information such as the product name, the alcohol %, the volume ml and room for ean code. The bottle needs to be sealed for shipment, so a little seal to cover the lid is required.
Nice to have
• It would be nice to maintain consistency with for example the same animal but change of background / colors / outfit / etc to clarify the different flavors. A cutout/contour is also preferable for added interest, so that the label is not square.
Should not have
• The label should definitely not be childish or too much. The overal look and feel needs to be professional yet not too serious.

```html
<!DOCTYPE html>
<html lang="en">
<head>
<meta charset="utf-8">
<title>Tipplefoxes Gently Smoked – Wraparound Label</title>
<link href="https://fonts.googleapis.com/css2?family=Josefin+Sans:wght@300;400&family=Oswald:wght@400&display=swap" rel="stylesheet">
<style>
  :root {
    --page: #ffffff;
    --lavender: #e7d5fb;
    --glow: #fdfbff;
    --gold: #d7bf62;
    --gold-light: #eedc8c;
    --ink: #111111;
    --herb-green: #4f6a34;
    --herb-violet: #7c68c9;
    --fur: #b58b5c;
  }
  * { margin: 0; padding: 0; box-sizing: border-box; }
  html, body { width: 1200px; height: 503px; overflow: hidden; background: var(--page); }
  .canvas { position: relative; width: 1200px; height: 503px; }

  .dimension-lines { position: absolute; inset: 0; }
  .dimension-label {
    position: absolute;
    font-family: "Oswald", sans-serif;
    font-size: 17px;
    letter-spacing: 3px;
    color: var(--ink);
  }
  .dimension-width { left: 553px; top: 47px; }
  .dimension-height { left: 1098px; top: 266px; }

  .label {
    position: absolute;
    left: 138px; top: 113px;
    width: 916px; height: 330px;
    background: radial-gradient(ellipse 230px 190px at 440px 140px, var(--glow) 0%, #f1e6fd 45%, var(--lavender) 100%);
    overflow: hidden;
  }
  .gold-band {
    position: absolute; left: 0; width: 100%; height: 5px;
    background: linear-gradient(90deg, var(--gold) 0%, var(--gold-light) 30%, var(--gold) 60%, var(--gold-light) 100%);
  }
  .gold-band.top { top: 17px; }
  .gold-band.bottom { top: 309px; }
  .trim-frame {
    position: absolute; left: 10px; top: 10px; width: 896px; height: 311px;
    border: 1.5px solid var(--ink);
  }

  .herb-bundle-faint {
    position: absolute; left: 40px; top: 23px; width: 235px; height: 258px;
    background: radial-gradient(ellipse at 45% 55%, rgba(140,154,120,0.35), rgba(185,160,200,0.18) 60%, transparent 75%);
    border-radius: 40% 60% 45% 55%;
  }
  .story {
    position: absolute; left: 20px; top: 53px; width: 210px;
    font-family: "Josefin Sans", sans-serif; font-weight: 400;
    font-size: 13px; line-height: 16px; letter-spacing: 1.9px;
    text-align: center; color: var(--ink); white-space: nowrap;
  }

  .mascot {
    position: absolute; left: 352px; top: 28px; width: 141px; height: 206px;
    background: linear-gradient(180deg, var(--fur) 0%, #a9804f 38%, #5d5a2e 60%, var(--herb-green) 100%);
    border-radius: 40% 40% 30% 30% / 30% 30% 18% 18%;
    opacity: 0.85;
  }
  .series-mark {
    position: absolute; left: 352px; top: 29px; width: 141px;
    text-align: center;
    font-family: "Josefin Sans", sans-serif; font-weight: 400;
    font-size: 7px; letter-spacing: 0.8px; line-height: 9px; color: var(--ink);
  }

  .brand-block { position: absolute; left: 330px; top: 236px; width: 216px; text-align: center; }
  .brand-name {
    font-family: "Josefin Sans", sans-serif; font-weight: 400;
    font-size: 21px; letter-spacing: 1.6px; line-height: 22px; color: var(--ink);
  }
  .flavour {
    font-family: "Josefin Sans", sans-serif; font-weight: 300;
    font-size: 16px; letter-spacing: 2.4px; line-height: 20px; color: var(--gold);
  }
  .spec-row {
    position: absolute; left: 352px; top: 277px; height: 27px;
    display: flex; align-items: center;
    font-family: "Josefin Sans", sans-serif; color: var(--ink);
  }
  .abv { color: var(--gold); width: 48px; }
  .abv-value { display: block; font-size: 14px; letter-spacing: 1.6px; line-height: 14px; }
  .abv-unit { display: block; font-size: 9.5px; letter-spacing: 1px; line-height: 11px; }
  .divider { width: 1px; height: 27px; background: var(--ink); margin: 0 4px; }
  .category { font-size: 11.5px; letter-spacing: 1.5px; line-height: 14px; width: 58px; }
  .volume { font-size: 17px; letter-spacing: 2px; padding-top: 3px; }

  .herb-sprig {
    position: absolute; left: 669px; top: 68px; width: 180px; height: 133px;
    background: radial-gradient(ellipse at 55% 55%, var(--herb-violet) 0%, var(--herb-green) 45%, rgba(79,106,52,0.2) 70%, transparent 78%);
    border-radius: 50%;
  }
  .tasting-note {
    position: absolute; left: 642px; top: 209px; width: 240px;
    font-family: "Josefin Sans", sans-serif;
    font-size: 14px; line-height: 17.5px; letter-spacing: 2.3px;
    text-align: center; color: var(--ink); white-space: nowrap;
  }
</style>
</head>
<body>
<div class="canvas">
  <svg class="dimension-lines" width="1200" height="503" viewBox="0 0 1200 503" aria-hidden="true">
    <polyline points="148,107 148,74 1044,74 1044,107" fill="none" stroke="#111" stroke-width="1.6"/>
    <polyline points="1058,123 1091,123 1091,434 1058,434" fill="none" stroke="#111" stroke-width="1.6"/>
  </svg>
  <div class="dimension-label dimension-width">260mm</div>
  <div class="dimension-label dimension-height">90mm</div>

  <section class="label">
    <div class="gold-band top"></div>
    <div class="gold-band bottom"></div>

    <div class="herb-bundle-faint" role="img" aria-label="Faint illustration of two tied bundles of rosemary"></div>
    <p class="story">While searching for an<br>upright yet surprising<br>spirit, our bartenders<br>stumbled upon a serious<br>challenge.<br>A new idea came to life!<br>The shaker lineup<br>were made by and for<br>mixologist, not excluding<br>all those seeking spiritual<br>entlightment.</p>

    <div class="mascot" role="img" aria-label="Illustration of a French bulldog in a rosemary-patterned suit holding a pink cocktail"></div>
    <p class="series-mark">THE SHAKER LINEUP</p>

    <div class="brand-block">
      <h1 class="brand-name">TIPPLEFOXES</h1>
      <p class="flavour">GENTLY SMOKED</p>
    </div>
    <div class="spec-row">
      <div class="abv"><span class="abv-value">37.5%</span><span class="abv-unit">vol.alc.</span></div>
      <div class="divider"></div>
      <div class="category">Blended<br>Spirit</div>
      <div class="divider"></div>
      <div class="volume">500ml</div>
    </div>

    <div class="herb-sprig" role="img" aria-label="Illustration of a rosemary sprig with violet flowers"></div>
    <p class="tasting-note">Finely distilled vodka<br>with a smoked<br>rosemary finish.</p>

    <div class="trim-frame"></div>
  </section>
</div>
</body>
</html>
```